Savings/Retirement Infographic

I need an infographic to convey the importance of retirement planning and saving regularly. It must be an attractive and compelling design that people want to read.

The design will primarily be used as a poster, but also as an emailer and a shorter version for an A5 flyer.

Content:

There are only two types of retirement funds
Big or Small

Big retirement funds = Foreign Travel,
Sailing,
Concerts,
Sky Diving,
Fishing,
Golf,
Fine Dining,
Spoiling Grandchildren,
Sandy Beaches.

Small retirement funds = Counting every penny,
Sitting at home,
Relying on family, friends and charity,
Turning off the heating in Winter

Big pensions are acquired over the length of a career with careful planning and motivation.

Small pensions take no effort at all.

Which are you aiming for?

Did you know?
1 in 5 people retiring in 2013 will be below the poverty line?
In the UK, 14% will rely solely on a state pension. That's less than AED 640 per week.
(Source: Harrowgate Cohort of 2013)

Of 100 people aged 25 today, by age 65
1 will be wealthy
4 will be financially independent
5 will still be working
12 will be bankrupt
29 will already be dead
49 will be dependent on others

Of those still living, 86% will rely on friends, relatives and charity.

To retire on $30,000 per annum, you'll need approx.. $600,000 in today's terms.
That's $1,456,380 in 30 years with 3% inflation.
By saving in a bank earning ZERO interest, you need to save $4,045 each month for 30 years
If you invest in the markets and earn 5% interest each year, you only need to save $2,307 each month.
If you manage to get 10% per annum interest, you'll only need to save $934 per month. That's less than AED 3,450.

Please add a bar across the bottom with my contact details, leaving space for my photo and logo. Contact details:

E: rmoss@tidalnest.com
M: 050 8126 473

```html
<!DOCTYPE html>
<html lang="en">
<head>
<meta charset="utf-8">
<title>Retirement Funds – Big or Small</title>
<link href="https://fonts.googleapis.com/css2?family=Montserrat:wght@400;500;600;700&display=swap" rel="stylesheet">
<style>
:root{
  --orange:#f59d5c;
  --teal:#7aaab8;
  --panel:#e9edf0;
  --band:#d6dbdf;
  --ink:#2b3540;
  --grey-text:#3d4650;
  --blue:#1f6fb0;
  --blue-head:#2a7cc0;
  --green:#1ea73a;
  --gold:#b8892a;
  --num-orange:#ec7a2c;
  --purple:#8270c4;
  --stats-bg:#eef1f4;
  --table-side:#9dbccb;
  --table-bg:#cfe1e9;
  --white:#ffffff;
  --placeholder:#d9dee2;
}
*{margin:0;padding:0;box-sizing:border-box}
html,body{width:849px;height:1200px;overflow:hidden;background:var(--white)}
body{font-family:"Montserrat",sans-serif;color:var(--grey-text)}
.poster{position:relative;width:849px;height:1200px;overflow:hidden;background:var(--white)}
.abs{position:absolute}

/* header */
.head-big{left:0;top:0;width:424px;height:144px;background:var(--orange)}
.head-small{left:424px;top:0;width:425px;height:144px;background:var(--teal)}
.title{left:0;width:849px;top:14px;text-align:center;font-weight:600;font-size:32px;letter-spacing:4px;color:var(--ink)}
.word-big{left:236px;top:54px;font-weight:700;font-size:60px;color:var(--white);letter-spacing:1px}
.word-small{left:450px;top:76px;font-weight:700;font-size:40px;color:var(--white);letter-spacing:2px}

/* lists */
.list-panel{left:0;top:144px;width:849px;height:226px;background:var(--panel)}
.divider{left:424px;top:144px;width:1px;height:291px;background:#cdd3d8}
.list{list-style:none;font-weight:600;font-size:15px;color:var(--ink);line-height:22.2px;white-space:nowrap}
.list li::before{content:"•";margin-right:8px}
.list-big{left:98px;top:157px}
.list-small{left:504px;top:155px;line-height:26.6px}
.list-small .cont{padding-left:15px}
.list-small .cont::before{content:""}
.summary-band{left:0;top:370px;width:849px;height:65px;background:var(--band)}
.summary{top:386px;font-size:24px;color:var(--ink);letter-spacing:.5px}
.summary-big{left:22px}
.summary-small{left:518px}

/* illustration areas */
.illus{border-radius:10px}

/* aim */
.aim{left:204px;top:454px;width:418px;text-align:center;font-weight:700;font-size:23.5px;color:var(--blue-head);letter-spacing:.5px}
.aim-rule{left:204px;top:488px;width:418px;height:2px;background:#a9b0b6}

.poverty{left:204px;top:522px;font-size:15.5px;line-height:21px}
.poverty em{font-style:normal;color:var(--gold)}
.pct-14{left:418px;top:506px;font-weight:700;font-size:58px;color:var(--green);line-height:1}
.pct-14 sup{font-size:24px;font-weight:500;vertical-align:top;position:relative;top:2px}
.in-uk{left:430px;top:572px;font-weight:600;font-size:12.5px;color:var(--ink)}
.state-text{left:520px;top:521px;font-size:15.5px;line-height:21px}
.source{left:521px;top:571px;font-size:9px;color:var(--ink)}

/* stats */
.stats-band{left:0;top:620px;width:849px;height:212px;background:var(--stats-bg)}
.stats-rule{left:0;top:752px;width:849px;height:1px;background:var(--white)}
.of-100{left:30px;top:658px;width:150px;text-align:right;font-size:16.5px;line-height:21px}
.stat{top:636px;width:110px;text-align:center;color:var(--blue)}
.stat b{display:block;font-weight:700;font-size:50px;line-height:60px}
.stat span{display:block;font-weight:500;font-size:15px;line-height:21px;color:var(--grey-text)}
.of-those{left:50px;top:774px;font-size:16.5px;line-height:21px}
.pct-86{left:146px;top:768px;font-weight:700;font-size:50px;color:var(--num-orange);line-height:1}
.pct-86 sup{font-size:22px;font-weight:500;vertical-align:top;position:relative;top:2px}
.rely{left:250px;top:783px;font-size:16.5px}

/* money */
.retire-on{left:30px;top:860px;width:142px;text-align:center;font-weight:600;font-size:15px;color:var(--ink);letter-spacing:.5px}
.sum{font-weight:600;color:var(--purple);line-height:1}
.sum small{font-size:.6em;vertical-align:top;position:relative;top:3px}
.sum-30k{left:40px;top:882px;font-size:30px}
.per-annum{left:60px;top:910px;font-size:15px;color:var(--ink)}
.need{left:244px;top:862px;font-size:15.5px;color:var(--ink)}
.sum-600k{left:242px;top:884px;font-size:35px}
.thats{left:464px;top:884px;font-weight:600;font-size:15px;letter-spacing:3px;color:var(--ink)}
.sum-big{left:572px;top:858px;font-weight:600;font-size:45px;color:var(--num-orange);line-height:1}
.sum-big small{font-size:22px;vertical-align:top;position:relative;top:4px}
.inflation{left:566px;top:905px;font-size:16px;color:var(--ink);letter-spacing:.3px}

/* table */
.table-bg{left:0;top:948px;width:849px;height:156px;background:var(--table-bg)}
.table-side{left:0;top:948px;width:186px;height:156px;background:var(--table-side)}
.table-hrule{left:0;top:1029px;width:708px;height:1px;background:var(--white)}
.table-vrule{top:948px;width:1px;height:156px;background:var(--white)}
.side-label{left:0;width:186px;font-weight:600;font-size:16px;line-height:21px;color:var(--white)}
.rate{top:960px;width:140px;text-align:center;font-weight:700;font-size:46px;color:var(--blue);line-height:60px}
.rate sup{font-size:22px;font-weight:500;vertical-align:top;position:relative;top:-4px}
.saving{top:1040px;width:160px;text-align:center;font-weight:700;font-size:38px;color:var(--green);line-height:50px}
.saving small{font-size:17px;vertical-align:top;position:relative;top:-4px}

/* contact */
.photo-slot{left:34px;top:1112px;width:76px;height:76px;background:var(--placeholder)}
.contact{left:130px;top:1138px;font-weight:500;font-size:13.5px;line-height:21px;color:var(--ink)}
.logo-slot{left:642px;top:1113px;width:164px;height:75px;background:var(--placeholder);display:flex;align-items:center;justify-content:center;font-size:16px;color:var(--ink)}
</style>
</head>
<body>
<div class="poster">

  <!-- header -->
  <div class="abs head-big"></div>
  <div class="abs head-small"></div>
  <div class="abs title">RETIREMENT FUNDS</div>
  <div class="abs word-big">BIG</div>
  <div class="abs word-small">SMALL</div>
  <div class="abs illus" role="img" aria-label="Piggy bank with a gold coin dropping in" style="left:688px;top:8px;width:112px;height:150px;background:linear-gradient(180deg,#f3c23a 0%,#f5a08a 35%,#ef8e78 100%)"></div>

  <!-- lists -->
  <div class="abs list-panel"></div>
  <div class="abs divider"></div>
  <div class="abs illus" role="img" aria-label="Orange aeroplane with a flight trail" style="left:2px;top:126px;width:84px;height:96px;background:linear-gradient(160deg,#f08a4a,#e9edf0)"></div>
  <div class="abs illus" role="img" aria-label="Golf green with a red flag and ball" style="left:10px;top:262px;width:76px;height:96px;background:linear-gradient(180deg,#ee6a3a 0%,#a8d44a 55%,#7fbf35 100%)"></div>
  <div class="abs illus" role="img" aria-label="Dolphin leaping beside a palm tree island" style="left:306px;top:222px;width:110px;height:154px;background:linear-gradient(180deg,#9fd0ec 0%,#5fb845 45%,#f1c34a 85%,#cfe9f5 100%)"></div>
  <ul class="abs list list-big">
    <li>Foreign Travel</li><li>Sailing</li><li>Concerts</li><li>Sky Diving</li><li>Fishing</li><li>Golf</li><li>Fine Dining</li><li>Spoiling Grandchildren</li><li>Sandy Beaches</li>
  </ul>
  <div class="abs illus" role="img" aria-label="Gold coin" style="left:448px;top:180px;width:34px;height:40px;border-radius:50%;background:linear-gradient(180deg,#f7cd45,#e3a51c)"></div>
  <svg class="abs" style="left:442px;top:236px" width="50" height="54" viewBox="0 0 50 54" aria-hidden="true">
    <g fill="#6fb5cb"><circle cx="12" cy="6" r="5"/><rect x="5" y="13" width="14" height="22" rx="3"/><rect x="6" y="33" width="5" height="20"/><rect x="13" y="33" width="5" height="20"/>
    <circle cx="37" cy="6" r="5"/><rect x="30" y="13" width="14" height="22" rx="3"/><rect x="31" y="33" width="5" height="20"/><rect x="38" y="33" width="5" height="20"/></g>
  </svg>
  <ul class="abs list list-small">
    <li>Counting Every Penny</li><li>Sitting at Home</li><li>Relying on Family,</li><li class="cont">Friends and Charity</li><li>Turning off the</li><li class="cont">Heating in Winter</li>
  </ul>
  <div class="abs illus" role="img" aria-label="Small house and an elderly woman in a wheelchair" style="left:694px;top:212px;width:112px;height:164px;background:linear-gradient(180deg,#8a5a45 0%,#f4efe6 35%,#f2d23a 65%,#c9463c 100%)"></div>

  <div class="abs summary-band"></div>
  <div class="abs summary summary-big">careful planning &amp; motivation</div>
  <div class="abs summary summary-small">no effort</div>

  <!-- aim -->
  <div class="abs aim">WHICH ARE YOU AIMING FOR?</div>
  <div class="abs aim-rule"></div>

  <svg class="abs" style="left:38px;top:520px" width="152" height="58" viewBox="0 0 152 58" aria-hidden="true">
    <g fill="#1f6fb0"><circle cx="14" cy="6" r="5.5"/><rect x="6" y="13" width="16" height="24" rx="3"/><rect x="7" y="35" width="6" height="22"/><rect x="15" y="35" width="6" height="22"/></g>
    <g fill="#cfd3d7">
      <circle cx="45" cy="6" r="5.5"/><rect x="37" y="13" width="16" height="24" rx="3"/><rect x="38" y="35" width="6" height="22"/><rect x="46" y="35" width="6" height="22"/>
      <circle cx="76" cy="6" r="5.5"/><rect x="68" y="13" width="16" height="24" rx="3"/><rect x="69" y="35" width="6" height="22"/><rect x="77" y="35" width="6" height="22"/>
      <circle cx="107" cy="6" r="5.5"/><rect x="99" y="13" width="16" height="24" rx="3"/><rect x="100" y="35" width="6" height="22"/><rect x="108" y="35" width="6" height="22"/>
      <circle cx="138" cy="6" r="5.5"/><rect x="130" y="13" width="16" height="24" rx="3"/><rect x="131" y="35" width="6" height="22"/><rect x="139" y="35" width="6" height="22"/>
    </g>
  </svg>
  <div class="abs poverty">1 in 5 people retiring in<br>2013 will be below<br>the <em>poverty line?</em></div>
  <div class="abs pct-14">14<sup>%</sup></div>
  <div class="abs in-uk">In the UK</div>
  <div class="abs state-text">will rely solely on a state pension.<br>That's less than AED 640/week.</div>
  <div class="abs source">(Source: Harrowgate Cohort of 2013)</div>

  <!-- stats -->
  <div class="abs stats-band"></div>
  <div class="abs stats-rule"></div>
  <div class="abs of-100">Of 100 people<br>aged 25 today,<br>by age 65</div>
  <div class="abs stat" style="left:187px"><b>1</b><span>wealthy</span></div>
  <div class="abs stat" style="left:289px"><b>4</b><span>financially<br>independent</span></div>
  <div class="abs stat" style="left:389px"><b>5</b><span>still be<br>working</span></div>
  <div class="abs stat" style="left:491px"><b>12</b><span>bankrupt</span></div>
  <div class="abs stat" style="left:591px"><b>29</b><span>already<br>be dead</span></div>
  <div class="abs stat" style="left:691px"><b>49</b><span>dependent<br>on others</span></div>

  <div class="abs of-those">Of those<br>still living</div>
  <div class="abs pct-86">86<sup>%</sup></div>
  <div class="abs rely">will rely on friends, relatives and charity</div>
  <svg class="abs" style="left:610px;top:760px" width="52" height="56" viewBox="0 0 50 54" aria-hidden="true">
    <g fill="#6fb5cb"><circle cx="12" cy="6" r="5"/><rect x="5" y="13" width="14" height="22" rx="3"/><rect x="6" y="33" width="5" height="20"/><rect x="13" y="33" width="5" height="20"/>
    <circle cx="37" cy="6" r="5"/><rect x="30" y="13" width="14" height="22" rx="3"/><rect x="31" y="33" width="5" height="20"/><rect x="38" y="33" width="5" height="20"/></g>
  </svg>

  <!-- money -->
  <div class="abs retire-on">TO RETIRE ON</div>
  <div class="abs sum sum-30k"><small>$</small>30,000</div>
  <div class="abs per-annum">per annum</div>
  <div class="abs need">you'll need approx..</div>
  <div class="abs sum sum-600k"><small>$</small>600,000</div>
  <div class="abs thats">THAT'S</div>
  <div class="abs sum-big"><small>$</small>1,456,380</div>
  <div class="abs inflation">in 30 years with 3% inflation</div>

  <!-- savings table -->
  <div class="abs table-bg"></div>
  <div class="abs table-side"></div>
  <div class="abs table-hrule"></div>
  <div class="abs table-vrule" style="left:372px"></div>
  <div class="abs table-vrule" style="left:534px"></div>
  <div class="abs side-label" style="top:975px;padding-left:33px">Interest rate<br>per annum</div>
  <div class="abs side-label" style="top:1043px;text-align:right;padding-right:24px">savings needed<br>per month</div>
  <div class="abs rate" style="left:212px">0<sup>%</sup></div>
  <div class="abs rate" style="left:388px">5<sup>%</sup></div>
  <div class="abs rate" style="left:550px;font-size:50px">10<sup>%</sup></div>
  <div class="abs saving" style="left:200px"><small>$</small>4,045</div>
  <div class="abs saving" style="left:374px"><small>$</small>2,307</div>
  <div class="abs saving" style="left:528px"><small>$</small>934</div>
  <div class="abs illus" role="img" aria-label="Sack overflowing with gold coins" style="left:708px;top:950px;width:110px;height:150px;background:linear-gradient(180deg,#efe3b0 0%,#f2c53a 55%,#dca524 100%)"></div>

  <!-- contact bar -->
  <div class="abs photo-slot" role="img" aria-label="Space for portrait photo"></div>
  <div class="abs contact">E: rmoss@tidalnest.com<br>M: 050 8126 473</div>
  <div class="abs logo-slot">Logo</div>

</div>
</body>
</html>
```